Funky Cup design on our hot disposable cups

I would like two examples: one orange cup (like our logo color) with white writing, one white cup with orange writing:
On the top: Organic coffee because we care
Middle: Our logo (attached but drop the R in the circle)
Bottom: Live Life Like a Tinker
Would love ideas what else can be written or patterned around the cup, clever design such as Coffee moorings or any other funky ideas.

It should include the text "tinkers & tide " all over the cup around the logo!

thanks.

Target Market(s)

female and male 17 to 30s

Industry/Entity Type

Coffee

Font styles to use
Other font styles liked:
• Galano grotesque like our logosame as logo

Colors
EE7325
F08F49
F5BC92
FAE3D3
FDF4ED

Requirements
Must have
• cool fun , trendy look. It should include the text "tinkers & tide " all over the cup around the logo!
Should not have
• in my logo please drop the r with the circle

```html
<!DOCTYPE html>
<html lang="en">
<head>
<meta charset="utf-8">
<title>tinkers &amp; tide — cup wraps</title>
<link href="https://fonts.googleapis.com/css2?family=Outfit:wght@500;600;700&display=swap" rel="stylesheet">
<style>
  :root {
    --brand-orange: #EE7325;
    --orange-mid: #F08F49;
    --orange-soft: #F5BC92;
    --orange-pale: #FAE3D3;
    --cream: #FDF4ED;
    --wrap-white: #F6F6F8;
    --page: #FFFFFF;
    --white: #FFFFFF;
  }
  * { box-sizing: border-box; margin: 0; padding: 0; }
  html, body { width: 1200px; height: 1200px; overflow: hidden; background: var(--page); }
  body { font-family: "Outfit", sans-serif; position: relative; }

  .cup-wrap {
    position: absolute;
    left: 80px;
    width: 1040px;
    height: 450px;
    display: flex;
  }
  .cup-wrap--white { top: 120px; background: var(--wrap-white); color: var(--brand-orange); }
  .cup-wrap--orange { top: 630px; background: var(--brand-orange); color: var(--white); }
  .cup-wrap--orange .wrap-panel + .wrap-panel { border-left: 1px solid rgba(255,255,255,0.15); }

  .wrap-panel { position: relative; width: 520px; height: 450px; overflow: hidden; }

  .leaf-art { position: absolute; border-radius: 50% 50% 45% 45%; }
  .cup-wrap--white .leaf-art { background: radial-gradient(circle at 50% 40%, var(--brand-orange), var(--orange-mid)); }
  .cup-wrap--orange .leaf-art { background: radial-gradient(circle at 50% 40%, var(--white), var(--orange-pale)); }
  .leaf-art--top-left { left: 14px; top: -20px; width: 125px; height: 147px; }
  .leaf-art--top-right { left: 380px; top: -10px; width: 86px; height: 83px; }
  .leaf-art--mid-right { left: 369px; top: 170px; width: 83px; height: 84px; }
  .leaf-art--left { left: 9px; top: 275px; width: 84px; height: 84px; }
  .leaf-art--bottom-right { left: 380px; top: 327px; width: 121px; height: 123px; }

  .headline { position: absolute; left: 0; right: 0; top: 42px; text-align: center; line-height: 1; }
  .headline__organic { display: block; font-size: 56px; font-weight: 700; letter-spacing: -0.5px; }
  .headline__coffee { display: block; font-size: 28px; font-weight: 700; margin-top: -2px; }
  .headline__care { display: block; font-size: 16px; font-weight: 600; margin-top: -3px; }

  .brand-name {
    position: absolute; left: 0; right: 0; top: 246px;
    display: flex; align-items: center; justify-content: center; gap: 10px;
    font-size: 30px; font-weight: 700;
  }
  .brand-name__dot { width: 22px; height: 22px; border-radius: 50%; background: currentColor; }

  .tagline { position: absolute; left: 0; right: 0; top: 388px; text-align: center; font-size: 16px; font-weight: 600; }
</style>
</head>
<body>

<section class="cup-wrap cup-wrap--white" aria-label="White cup wrap with orange print">
  <div class="wrap-panel">
    <div class="leaf-art leaf-art--top-left" role="img" aria-label="Orange leaf sprig illustration"></div>
    <div class="leaf-art leaf-art--top-right" role="img" aria-label="Orange leaf sprig illustration"></div>
    <div class="leaf-art leaf-art--mid-right" role="img" aria-label="Orange leaf sprig illustration"></div>
    <div class="leaf-art leaf-art--left" role="img" aria-label="Orange leaf sprig illustration"></div>
    <div class="leaf-art leaf-art--bottom-right" role="img" aria-label="Orange leaf sprig illustration"></div>
    <h2 class="headline"><span class="headline__organic">organic</span><span class="headline__coffee">coffee</span><span class="headline__care">because we care</span></h2>
    <div class="brand-name"><span class="brand-name__dot"></span>tinkers &amp; tide</div>
    <p class="tagline">live life like a tinker</p>
  </div>
  <div class="wrap-panel">
    <div class="leaf-art leaf-art--top-left" role="img" aria-label="Orange leaf sprig illustration"></div>
    <div class="leaf-art leaf-art--top-right" role="img" aria-label="Orange leaf sprig illustration"></div>
    <div class="leaf-art leaf-art--mid-right" role="img" aria-label="Orange leaf sprig illustration"></div>
    <div class="leaf-art leaf-art--left" role="img" aria-label="Orange leaf sprig illustration"></div>
    <div class="leaf-art leaf-art--bottom-right" role="img" aria-label="Orange leaf sprig illustration"></div>
    <h2 class="headline"><span class="headline__organic">organic</span><span class="headline__coffee">coffee</span><span class="headline__care">because we care</span></h2>
    <div class="brand-name"><span class="brand-name__dot"></span>tinkers &amp; tide</div>
    <p class="tagline">live life like a tinker</p>
  </div>
</section>

<section class="cup-wrap cup-wrap--orange" aria-label="Orange cup wrap with white print">
  <div class="wrap-panel">
    <div class="leaf-art leaf-art--top-left" role="img" aria-label="White leaf sprig illustration"></div>
    <div class="leaf-art leaf-art--top-right" role="img" aria-label="White leaf sprig illustration"></div>
    <div class="leaf-art leaf-art--mid-right" role="img" aria-label="White leaf sprig illustration"></div>
    <div class="leaf-art leaf-art--left" role="img" aria-label="White leaf sprig illustration"></div>
    <div class="leaf-art leaf-art--bottom-right" role="img" aria-label="White leaf sprig illustration"></div>
    <h2 class="headline"><span class="headline__organic">organic</span><span class="headline__coffee">coffee</span><span class="headline__care">because we care</span></h2>
    <div class="brand-name"><span class="brand-name__dot"></span>tinkers &amp; tide</div>
    <p class="tagline">live life like a tinker</p>
  </div>
  <div class="wrap-panel">
    <div class="leaf-art leaf-art--top-left" role="img" aria-label="White leaf sprig illustration"></div>
    <div class="leaf-art leaf-art--top-right" role="img" aria-label="White leaf sprig illustration"></div>
    <div class="leaf-art leaf-art--mid-right" role="img" aria-label="White leaf sprig illustration"></div>
    <div class="leaf-art leaf-art--left" role="img" aria-label="White leaf sprig illustration"></div>
    <div class="leaf-art leaf-art--bottom-right" role="img" aria-label="White leaf sprig illustration"></div>
    <h2 class="headline"><span class="headline__organic">organic</span><span class="headline__coffee">coffee</span><span class="headline__care">because we care</span></h2>
    <div class="brand-name"><span class="brand-name__dot"></span>tinkers &amp; tide</div>
    <p class="tagline">live life like a tinker</p>
  </div>
</section>

</body>
</html>
```